Social media adds needed for our STELLAR TONE VOYAGE @ THE MERIDIAN STARDOME

We are needing Social Media ads (IG & FB) for a Sound Bath at THE MERIDIAN STARDOME. Here is a link to the Event,
https://www.rubenosoriotones.example/events/p/stardome-mer-71835-kqwzd
It needs to state "RUBEN OSORIO TONES presents"
"STELLAR TONE VOYAGE @ THE MERIDIAN STARDOME" date, time and address for the event should be included, but not the price.
Saturday, August 17, 2024 7:00-8:30 pm
Location: Meridian Stardome - 2250 Larkfield Ave, Vancouver, BC
It needs to include a photo of the Stardome (2 options attached) and include Ruben (several photo options attached). Also attached is a photo of the show performed which could also be incorporated

```html
<!DOCTYPE html>
<html lang="en">
<head>
<meta charset="utf-8">
<title>Stellar Tone Voyage — Ruben Osorio Tones</title>
<link rel="stylesheet" href="https://fonts.googleapis.com/css2?family=League+Spartan:wght@700;800&family=Poppins:wght@300;500;600;700&display=swap">
<style>
  :root {
    --bg-deep: #1b0f72;
    --bg-mid: #2c1cb4;
    --bg-glow: #3a2ad0;
    --orange: #ff9a2e;
    --white: #ffffff;
    --violet-box: #4a1fff;
    --title-violet-a: #8d3dff;
    --title-violet-b: #5a2cf2;
    --title-blue-a: #3a9cf2;
    --title-blue-b: #8cc8ff;
    --brand-grey: #c9c4ea;
    --photo-light: #8f86d8;
    --photo-mid: #5d4fc4;
    --photo-dark: #34249a;
  }
  * { margin: 0; padding: 0; box-sizing: border-box; }
  html, body { width: 1200px; height: 1200px; overflow: hidden; background: #ececec; }
  .ad {
    position: relative;
    width: 1200px; height: 1200px;
    overflow: hidden;
    background:
      radial-gradient(ellipse 520px 420px at 300px 260px, rgba(110, 60, 200, .35), transparent 70%),
      radial-gradient(ellipse 700px 600px at 900px 300px, var(--bg-glow), transparent 75%),
      linear-gradient(180deg, var(--bg-mid) 0%, var(--bg-deep) 100%);
    font-family: "Poppins", sans-serif;
    color: var(--white);
  }
  .hero-photo {
    position: absolute;
    left: 480px; top: 490px;
    width: 720px; height: 710px;
    background: linear-gradient(160deg, var(--photo-light) 0%, var(--photo-mid) 50%, var(--photo-dark) 100%);
    -webkit-mask-image: linear-gradient(90deg, transparent 0%, #000 16%);
            mask-image: linear-gradient(90deg, transparent 0%, #000 16%);
  }
  .presenter {
    position: absolute; left: 60px; top: 60px;
    font-weight: 700; font-size: 41px; line-height: 1;
    color: var(--orange); letter-spacing: .5px;
  }
  .presents {
    position: absolute; left: 60px; top: 106px;
    font-weight: 500; font-size: 37px; line-height: 1;
    letter-spacing: 7px;
  }
  .title {
    position: absolute; left: 58px; top: 150px;
    font-family: "League Spartan", sans-serif;
    font-weight: 800; font-size: 156px; line-height: 123px;
    letter-spacing: -1px;
  }
  .title span {
    display: block;
    -webkit-background-clip: text; background-clip: text;
    color: transparent;
  }
  .title .line-1 { background-image: linear-gradient(100deg, var(--title-violet-a), var(--title-violet-b)); }
  .title .line-2, .title .line-3 { background-image: linear-gradient(100deg, var(--title-blue-a), var(--title-blue-b)); }
  .brand-mark {
    position: absolute; left: 830px; top: 66px; width: 300px;
    text-align: center;
    font-weight: 300; font-size: 30px; line-height: 36px;
    letter-spacing: 7px; color: var(--brand-grey);
  }
  .brand-mark .ring {
    display: block; width: 160px; height: 160px; margin: 0 auto 30px;
    border: 5px solid var(--brand-grey); border-radius: 50%;
  }
  .date-month {
    position: absolute; left: 59px; top: 568px;
    font-weight: 700; font-size: 60px; line-height: 1;
    color: var(--orange); letter-spacing: -.5px;
  }
  .date-year {
    position: absolute; left: 55px; top: 618px;
    font-weight: 500; font-size: 134px; line-height: 1;
    letter-spacing: -4px;
  }
  .time-box {
    position: absolute; left: 401px; top: 575px;
    width: 267px; height: 161px;
    background: linear-gradient(90deg, var(--violet-box) 75%, rgba(74, 31, 255, .3));
    font-weight: 700; font-size: 56px; line-height: 1;
    padding: 18px 0 0 26px;
  }
  .time-box .time-end { margin-top: 14px; }
  .time-box .to {
    position: absolute; left: 125px; top: 63px;
    width: 36px; height: 36px; border-radius: 50%;
    background: #160c3a;
    font-size: 15px; font-weight: 600;
    display: flex; align-items: center; justify-content: center;
  }
  .venue {
    position: absolute; left: 60px; top: 826px;
    font-weight: 700; font-size: 40px; line-height: 42px;
    color: var(--orange); letter-spacing: 7px;
  }
  .address {
    position: absolute; left: 60px; top: 910px;
    font-weight: 500; font-size: 36px; line-height: 42px;
  }
  .cta {
    position: absolute; left: 60px; top: 1072px;
    font-weight: 600; font-size: 28px; line-height: 1;
    letter-spacing: 7px;
  }
</style>
</head>
<body>
  <main class="ad">
    <div class="hero-photo" role="img" aria-label="Photo of Ruben seated cross-legged playing crystal singing bowls among candles, in front of the Meridian Stardome building at night"></div>

    <p class="presenter">RUBEN OSORIO TONES</p>
    <p class="presents">PRESENTS</p>

    <h1 class="title">
      <span class="line-1">STELLAR</span>
      <span class="line-2">TONE</span>
      <span class="line-3">VOYAGE</span>
    </h1>

    <div class="brand-mark">
      <span class="ring"></span>
      RUBEN OSORIO<br>TONES
    </div>

    <p class="date-month">AUGUST 17</p>
    <p class="date-year">2024</p>

    <div class="time-box">
      <p class="time-start">7:00 PM</p>
      <p class="time-end">8:30 PM</p>
      <span class="to">TO</span>
    </div>

    <p class="venue">MERIDIAN<br>STARDOME</p>
    <p class="address">2250 Larkfield Ave,<br>Vancouver, BC</p>

    <p class="cta">BOOK YOUR SEATS NOW!</p>
  </main>
</body>
</html>
```